Reefhollow Website and inner template.

New website design for an existing client. Need a home page design and a simplified inner page template design, I have included a txt document with the specifics for this website design/poject. I have copy and pasted the info below
Project Description: Website design ( home page with an inner page template ) for Reefhollow LLC
Current Website Address: https://reefhollowshop.example
Main navigation link: ( same as on current website with the exception of Links and Resources being removed )
Instruction/Courses
Rentals
Trips & Charters
Service & Repairs
Tank Fills
Home
Contact
About ( Company Info )
Events
Specials
Home page specifics:
As with all website lately, they requested a large "hero banner" or "slider image" above the fold just below the navigation. Examples
https://gallantcopperworks.example/
https://pixelheronstudio.example/
https://maplestonelodge.example/
In addition to the main navigation menu and hero banner, we need to highlight some important features/links on the home page
Social media icons for facebook and instagram
Store Hours
Contact Information in cluding phone numbers
Scuba Instruction/Courses Link highlight area
Scuba Rental Gear Link highlight area
Scuba Repair Service Link highlight area
Large content area. Needs to be large enoug to move over the existing content on the current website ( see link above )
Large section for "Snorkels, Masks, Fins - How to Fit & Care for them " . Currently that is the only page on the resources page. Since we are removing the resources page, we would like make this a stand alone page only accessible via the home page in a highlight area.
Other Notes:
I have attached the logo to the project.
IMPORTANT... ONLY USE GRAPHICS/IMAGES from pexlo imagery. ( https://www.pexloimagery.example/ ) This is important because we have an account with them so you can use the watermarked images then when I build the website I can easily purchase the licensing rights for those images. You dont' need an account to do searches, locate images and use the water marked image in the design.
Target Market(s)
Diving Lessons, Equipment repair and charters
Number of Pages Required
2 page
Requirements
Must have
- Please see attached txt document with all the project specifics
Nice to have
Should not have

```html
<!DOCTYPE html>
<html lang="en">
<head>
<meta charset="utf-8">
<title>Reefhollow – Full Service Scuba Equipment Repair &amp; Diving Shop</title>
<link rel="stylesheet" href="https://fonts.googleapis.com/css2?family=Barlow:wght@400;500;600;700&family=Barlow+Semi+Condensed:wght@600;700&display=swap">
<style>
:root{
  --blue:#0e4f92;
  --blue-dark:#0a3d73;
  --blue-bright:#2a7bd0;
  --red:#c4161c;
  --pale:#e6edf4;
  --pale-2:#dbe7f2;
  --ink:#2b2f36;
  --muted:#6d7785;
  --white:#fff;
}
*{box-sizing:border-box;margin:0;padding:0}
html,body{width:1200px;height:4141px;overflow:hidden}
body{position:relative;font-family:"Barlow",sans-serif;color:var(--ink);background:var(--white);font-size:13px;line-height:1.75}
.abs{position:absolute}
h1,h2,h3,h4{font-family:"Barlow Semi Condensed",sans-serif;font-weight:700;line-height:1.1}
.eyebrow{font-size:12px;color:var(--muted);text-transform:uppercase;letter-spacing:.3px}
.eyebrow.blue{color:var(--blue-bright)}
.title{color:var(--blue);font-size:32px;text-transform:uppercase}
.btn{display:inline-flex;align-items:center;justify-content:center;background:var(--red);color:var(--white);font-family:"Barlow Semi Condensed",sans-serif;font-weight:700;font-size:13px;text-transform:uppercase;text-decoration:none;box-shadow:0 4px 10px rgba(0,0,0,.15)}
.photo{display:block}

/* top bar */
.topbar{left:0;top:0;width:1200px;height:45px;background:#eef2f6}
.topbar .phone{left:161px;top:13px;font-size:11px;color:var(--blue);display:flex;gap:8px;align-items:center}
.brand{display:flex;align-items:center;gap:8px;font-family:"Barlow Semi Condensed",sans-serif;font-weight:700;color:var(--red);font-size:22px;text-transform:uppercase;letter-spacing:.2px}
.brand .mark{width:22px;height:22px;background:var(--red)}
.topbar .brand{left:540px;top:9px}
.social{display:flex;gap:8px}
.social span{width:20px;height:20px;background:var(--blue);display:block}
.topbar .social{left:990px;top:12px}

/* nav */
.nav{left:0;top:45px;width:1200px;height:75px;background:var(--blue)}
.nav ul{position:absolute;left:161px;width:877px;top:28px;display:flex;justify-content:space-between;list-style:none}
.nav a{color:var(--white);font-size:12px;font-weight:500;text-decoration:none;text-transform:uppercase}
.nav .active{border-bottom:3px solid var(--red);padding-bottom:5px}

/* hero */
.hero{left:0;top:120px;width:1200px;height:799px;background:linear-gradient(180deg,#1a6fb8 0%,#0d4d8a 35%,#0b3a63 65%,#123049 100%)}
.hero .welcome{left:0;width:1200px;top:240px;text-align:center;color:var(--white);font-size:13px;letter-spacing:5px;text-transform:uppercase}
.hero h1{position:absolute;left:0;width:1200px;top:270px;text-align:center;color:var(--white);font-size:53px;text-transform:uppercase;letter-spacing:.3px}
.hero .btn{position:absolute;left:532px;top:415px;width:135px;height:47px}

/* feature cards */
.features{left:161px;top:808px;width:877px;height:151px;display:flex;box-shadow:0 10px 25px rgba(0,0,0,.12)}
.feature{flex:1;padding:30px 34px 0}
.feature h3{font-family:"Barlow",sans-serif;font-size:16px;font-weight:700;display:flex;align-items:center;gap:12px;margin-bottom:12px}
.feature p{font-size:11px;line-height:2}
.feature .ico{width:34px;height:34px;flex:none}
.f-white{background:var(--white);color:var(--blue)}
.f-white p{color:var(--blue-bright)}
.f-blue{background:var(--blue);color:var(--white)}
.f-red{background:var(--red);color:var(--white)}

/* about */
.about .eyebrow{left:161px;top:1040px}
.about .title{position:absolute;left:161px;top:1062px}
.about .copy{left:161px;top:1118px;width:350px;font-size:12px;line-height:1.9}
.about .copy p{margin-bottom:12px}
.about .btn{position:absolute;left:161px;top:1404px;width:136px;height:47px}
.video{left:681px;top:1044px;width:354px;height:402px;overflow:hidden;background:linear-gradient(160deg,#a9cde9 0%,#4f93cf 45%,#1c5ea3 100%)}
.video .years{position:absolute;right:28px;bottom:22px;text-align:right;color:#bfe0ff;font-family:"Barlow Semi Condensed",sans-serif;font-weight:700;font-size:30px;line-height:1.15;text-transform:uppercase}
.play{left:648px;top:1200px;width:66px;height:66px}

/* services */
.services{left:0;top:1527px;width:1200px;height:401px;background:linear-gradient(180deg,#d6e7f4 0%,#cfe3f2 60%,#bed7ec 100%)}
.services .eyebrow{position:absolute;left:0;width:1200px;top:74px;text-align:center}
.services .title{position:absolute;left:0;width:1200px;top:94px;text-align:center;font-size:30px}
.svc{top:1707px;width:278px;height:416px;background:var(--white);border:1px solid #e3e8ee;text-align:center}
.svc .pic{height:222px}
.svc .badge{position:absolute;left:116px;top:200px;width:46px;height:46px;background:var(--red);display:flex;align-items:center;justify-content:center}
.svc h3{margin-top:54px;font-size:17px;color:var(--blue);text-transform:uppercase}
.svc p{margin:14px auto 0;width:200px;font-size:11.5px;line-height:2;color:var(--ink)}
.svc .more{display:inline-flex;gap:8px;align-items:center;margin-top:10px;font-size:11px;color:var(--blue-bright);text-transform:uppercase;text-decoration:none}
.svc.on{background:var(--blue);border-color:var(--blue)}
.svc.on h3,.svc.on p,.svc.on .more{color:var(--white)}
.svc.on .badge{background:var(--white)}

/* snorkel */
.snorkel-pic{left:0;top:2198px;width:577px;height:577px;background:radial-gradient(ellipse at 40% 40%,#2a86c4 0%,#135d96 50%,#0a3a66 100%)}
.snorkel{left:622px;top:2198px;width:578px;height:577px;background:var(--pale)}
.snorkel .eyebrow{position:absolute;left:102px;top:74px;font-size:11px}
.snorkel h2{position:absolute;left:102px;top:94px;color:var(--blue);font-size:29px;text-transform:uppercase}
.snorkel .lead{position:absolute;left:102px;top:158px;width:340px;font-size:11.5px;line-height:1.9}
.snorkel ul{position:absolute;left:102px;top:215px;width:380px;list-style:none;font-size:11px;line-height:1.75}
.snorkel li{position:relative;padding-left:18px;margin-bottom:8px}
.snorkel li::before{content:"";position:absolute;left:0;top:4px;width:7px;height:7px;border:2px solid var(--red);border-radius:50%}
.snorkel .btn{position:absolute;left:102px;top:450px;width:135px;height:47px}

/* banner */
.banner{left:0;top:2820px;width:1200px;height:426px;background:linear-gradient(180deg,#1a5f9e 0%,#10508c 45%,#0d4277 100%)}
.banner h2{position:absolute;left:0;width:1200px;top:86px;text-align:center;color:var(--white);font-size:31px;line-height:1.25;text-transform:uppercase}
.banner p{position:absolute;left:0;width:1200px;top:222px;text-align:center;color:var(--white);font-size:14px}
.banner .btn{position:absolute;left:530px;top:288px;width:134px;height:48px}

/* partners + quote */
.partners .eyebrow{left:161px;top:3355px}
.partners h2{position:absolute;left:161px;top:3378px;color:var(--blue);font-size:31px;line-height:1.25;text-transform:uppercase}
.partners .copy{left:161px;top:3480px;width:340px;font-size:12px;line-height:1.9}
.badges{left:161px;top:3598px;display:flex;gap:12px}
.badges div{width:95px;height:58px;background:var(--white);border:1px solid #e3e8ee;display:flex;align-items:center;justify-content:center}
.badges span{display:block;width:64px;height:30px;background:var(--pale-2)}
.quote{left:656px;top:3230px;width:382px;height:538px;background:var(--pale)}
.quote h2{position:absolute;left:59px;top:58px;color:var(--blue);font-size:27px;text-transform:uppercase}
.quote .intro{position:absolute;left:59px;top:96px;width:260px;font-size:10px;line-height:1.8}
.quote .field{position:absolute;left:59px;width:263px;height:36px;background:var(--white);border:1px solid #d7dee6;padding:8px 10px;font-size:9px;color:#555}
.quote .area{height:88px}
.quote .btn{position:absolute;left:59px;top:450px;width:263px;height:40px;box-shadow:none}

/* footer */
.footer{left:0;top:3768px;width:1200px;height:322px;background:linear-gradient(180deg,#f1f5f9 0%,#e6eef5 100%)}
.footer .brand{position:absolute;left:161px;top:68px;font-size:20px}
.footer .about-text{position:absolute;left:161px;top:134px;width:220px;font-size:11px;line-height:2}
.footer .social{position:absolute;left:156px;top:240px}
.footer .social span{width:26px;height:26px}
.footer .social span:last-child{background:var(--red)}
.fcol{position:absolute;top:72px}
.fcol h4{color:var(--blue);font-size:17px;text-transform:uppercase;margin-bottom:28px}
.fcol ul{list-style:none;font-size:11px}
.fcol li{height:39px}
.fcol.hours li{display:flex;gap:12px;align-items:flex-start}
.copyright{left:0;top:4090px;width:1200px;height:51px;background:var(--blue);color:var(--white);font-size:11px;font-weight:600;text-align:center;line-height:51px}
</style>
</head>
<body>

<header>
  <div class="abs topbar">
    <div class="abs phone">
      <svg width="10" height="10" viewBox="0 0 24 24"><path fill="#0e4f92" d="M6.6 10.8a15 15 0 0 0 6.6 6.6l2.2-2.2a1 1 0 0 1 1-.25 11.4 11.4 0 0 0 3.6.57 1 1 0 0 1 1 1V20a1 1 0 0 1-1 1A17 17 0 0 1 3 4a1 1 0 0 1 1-1h3.5a1 1 0 0 1 1 1c0 1.25.2 2.45.57 3.6a1 1 0 0 1-.25 1z"/></svg>
      (860) - 555 - 0142 / (800) - 555 - 0198
    </div>
    <div class="abs brand"><span class="mark"></span>Reefhollow, LLC</div>
    <div class="abs social" aria-label="Social profiles"><span aria-label="Social profile one"></span><span aria-label="Social profile two"></span></div>
  </div>
  <nav class="abs nav">
    <ul>
      <li><a class="active" href="#">Home</a></li>
      <li><a href="#">About</a></li>
      <li><a href="#">Services</a></li>
      <li><a href="#">Rentals</a></li>
      <li><a href="#">Trips &amp; Charters</a></li>
      <li><a href="#">Tank Fills</a></li>
      <li><a href="#">Instructions/Courses</a></li>
      <li><a href="#">Events</a></li>
      <li><a href="#">Specials</a></li>
      <li><a href="#">Contact</a></li>
    </ul>
  </nav>
</header>

<section class="abs hero" role="img" aria-label="Scuba diver swimming above a deep blue coral reef">
  <div class="abs welcome">Welcome to Reefhollow</div>
  <h1>Full Service Scuba Equipment<br>Repair &amp; Scuba Diving Shop</h1>
  <a class="btn" href="#">View Courses</a>
</section>

<section class="abs features">
  <div class="feature f-white">
    <h3><svg class="ico" viewBox="0 0 34 34"><circle cx="17" cy="10" r="6" fill="none" stroke="#0e4f92" stroke-width="2"/><path d="M6 30c0-7 5-11 11-11s11 4 11 11" fill="none" stroke="#0e4f92" stroke-width="2"/></svg>Rescue &amp; Commercial</h3>
    <p>Lorem ipsum dolor sit amet, estetetiqua tetur adipiscing elit.</p>
  </div>
  <div class="feature f-blue">
    <h3><svg class="ico" viewBox="0 0 34 34"><path d="M4 26c4-3 8-3 13 0s9 3 13 0" fill="none" stroke="#fff" stroke-width="2"/><path d="M14 24V10M14 10c-5 0-8 3-8 3M14 10c5 0 8 3 8 3" fill="none" stroke="#fff" stroke-width="2"/><circle cx="27" cy="7" r="3" fill="none" stroke="#fff" stroke-width="2"/></svg>Scuba &amp; Exotic Travel</h3>
    <p>Lorem ipsum dolor sit amet, estetetiqua tetur adipiscing elit.</p>
  </div>
  <div class="feature f-red">
    <h3><svg class="ico" viewBox="0 0 34 34"><rect x="6" y="8" width="16" height="10" rx="4" fill="none" stroke="#fff" stroke-width="2"/><path d="M26 4v16a4 4 0 0 1-4 4h-4M4 28c4-3 8-3 13 0s9 3 13 0" fill="none" stroke="#fff" stroke-width="2"/></svg>Snorkeling &amp; Swimming</h3>
    <p>Lorem ipsum dolor sit amet, estetetiqua tetur adipiscing elit.</p>
  </div>
</section>

<section class="about">
  <div class="abs eyebrow">About Us</div>
  <h2 class="title">Welcome to Reefhollow</h2>
  <div class="abs copy">
    <p>Welcome to Reefhollow, a scuba and snorkeling shop located in the beautiful town of Saltmere Connecticut, in Saltmere Plaza which is across the street from The Saltmere Harbor Railway.</p>
    <p>Reefhollow has been servicing the scuba, snorkeling, spearfishing, and swimming communities for over 35 years! We carry a full line of equipment for your underwater adventures - from mask, fins, and snorkels to tanks, regulators, and suits. We have swim goggles and fins; spearfishing guns, bands, tips, and accessories; bags to carry your equipment; dive watches and computers; full face masks and books to read; and all types of equipment for the technical and rescue diver!</p>
  </div>
  <a class="btn" href="#">Discover More</a>
  <div class="abs video" role="img" aria-label="Group of divers at the water surface giving an okay signal">
    <svg class="abs" style="left:0;top:0" width="354" height="402" viewBox="0 0 354 402"><path d="M354 70C330 210 220 240 120 250 60 256 20 300 0 402h354z" fill="#0f4f93"/><path d="M354 110C330 240 230 265 130 272 70 277 25 320 8 402" fill="none" stroke="#fff" stroke-width="10"/></svg>
    <div class="years">35 Years<br>of Experience</div>
  </div>
  <svg class="abs play" viewBox="0 0 66 66" aria-label="Play video"><circle cx="33" cy="33" r="32" fill="#c4161c" stroke="#fff" stroke-width="2"/><path d="M27 22l17 11-17 11z" fill="#fff"/></svg>
</section>

<section class="abs services" role="img" aria-label="Soft underwater background with faint divers">
  <div class="eyebrow blue">Our Services List</div>
  <h2 class="title">What We Offer</h2>
</section>
<article class="abs svc" style="left:161px">
  <div class="pic photo" role="img" aria-label="Divers exploring a shipwreck in clear blue water" style="background:linear-gradient(160deg,#7cc4e6,#2d86bf 60%,#1a5f93)"></div>
  <div class="badge"><svg width="24" height="24" viewBox="0 0 24 24"><path d="M3 16c3-2 6-2 9 0s6 2 9 0M3 20c3-2 6-2 9 0s6 2 9 0M8 12l8-8" stroke="#fff" stroke-width="2" fill="none"/></svg></div>
  <h3>Scuba Courses</h3>
  <p>From entry level to Nitrox courses, we can help you explore underwater</p>
  <a class="more" href="#">Learn More <svg width="16" height="8" viewBox="0 0 16 8"><path d="M0 4h14M11 1l3 3-3 3" stroke="currentColor" fill="none"/></svg></a>
</article>
<article class="abs svc on" style="left:461px">
  <div class="pic photo" role="img" aria-label="Rack of wetsuits and buoyancy vests for rent" style="background:linear-gradient(180deg,#4a5d74,#23303f 70%,#16202b)"></div>
  <div class="badge"><svg width="24" height="24" viewBox="0 0 24 24"><rect x="6" y="4" width="7" height="16" rx="3" fill="none" stroke="#0e4f92" stroke-width="2"/><circle cx="17" cy="16" r="3" fill="none" stroke="#0e4f92" stroke-width="2"/></svg></div>
  <h3>Rental Gear</h3>
  <p>We offer a full line of scuba equipment for rental.</p>
  <a class="more" href="#">Learn More <svg width="16" height="8" viewBox="0 0 16 8"><path d="M0 4h14M11 1l3 3-3 3" stroke="currentColor" fill="none"/></svg></a>
</article>
<article class="abs svc" style="left:760px">
  <div class="pic photo" role="img" aria-label="Underwater camera housing held in blue water" style="background:linear-gradient(160deg,#5bb3e0,#1f79bb 60%,#125a94)"></div>
  <div class="badge"><svg width="24" height="24" viewBox="0 0 24 24"><circle cx="12" cy="12" r="4" fill="none" stroke="#fff" stroke-width="2.5"/><path d="M12 2v4M12 18v4M2 12h4M18 12h4M5 5l3 3M16 16l3 3M5 19l3-3M16 8l3-3" stroke="#fff" stroke-width="2.5"/></svg></div>
  <h3>Repair Service</h3>
  <p>Our trained technicians can repair your scuba equipment or dry suit.</p>
  <a class="more" href="#">Learn More <svg width="16" height="8" viewBox="0 0 16 8"><path d="M0 4h14M11 1l3 3-3 3" stroke="currentColor" fill="none"/></svg></a>
</article>

<div class="abs snorkel-pic photo" role="img" aria-label="Diver adjusting a mask at the water surface"></div>
<section class="abs snorkel">
  <div class="eyebrow blue">How to Fit &amp; Care for Them</div>
  <h2>Snorkels, Masks, Fins</h2>
  <p class="lead">Learn how to fit your snorkel/scuba mask and how to care and maintain your mask, snorkel &amp; fins.</p>
  <ul>
    <li>Fold the strap over the lenses</li>
    <li>Set the mask on your face without the strap</li>
    <li>Breathe in through your nose – like you're smelling perfume or flowers</li>
    <li>While breathing in, let go of the mask and look down</li>
    <li>If the mask stays on and you don't feel any air getting in, you have a good seal; which equals a great fit!</li>
    <li>If it seals well, put the mask on with the straps; adjust the strap just until it's comfortably snug. If the straps are over-tightened, the mask will be distorted on your face and not seal well.</li>
  </ul>
  <a class="btn" href="#">Discover More</a>
</section>

<section class="abs banner" role="img" aria-label="Split view of a boat hull above and below the water line">
  <h2>We at Reefhollow enjoy diving all over the<br>world and bringing groups to see the wonderful sights<br>both on land and underwater</h2>
  <p>See our <b>TRIP</b> page and sign up for your next adventure!</p>
  <a class="btn" href="#">Sign Up Now</a>
</section>

<section class="partners">
  <div class="abs eyebrow">Our Partners</div>
  <h2>Recognized by<br>Professionals</h2>
  <p class="abs copy">Lorem ipsum dolor sit amet, consectetur adipiscing elit, sed do eiusmod tempor incididunt ut labore et dolore magna aliqua. Ut enim ad minim veniam, quis nostrud exercitation ullamco laboris nisi ut aliquip ex ea commodo consequat.</p>
  <div class="abs badges" aria-label="Partner badges">
    <div><span></span></div><div><span></span></div><div><span></span></div><div><span></span></div>
  </div>
</section>

<section class="abs quote">
  <h2>Request a Quote</h2>
  <p class="intro">For a Drysuit Repair Service or Repair area - fill the form below to request a quote or ask a question of our service department!</p>
  <div class="field" style="top:162px">Your Name*</div>
  <div class="field" style="top:207px">Phone Number*</div>
  <div class="field" style="top:252px">Email Address*</div>
  <div class="field" style="top:297px">Brand/Model of Suit*</div>
  <div class="field area" style="top:342px">Additional Comments*</div>
  <a class="btn" href="#">Send Your Message</a>
</section>

<footer class="abs footer">
  <div class="brand"><span class="mark"></span>Reefhollow, LLC</div>
  <p class="about-text">Reefhollow has been servicing the scuba, snorkeling, spearfishing, and swimming communities for over 35 years!</p>
  <div class="social" aria-label="Social profiles"><span aria-label="Social profile one"></span><span aria-label="Social profile two"></span></div>
  <div class="fcol" style="left:459px"><h4>Quick Links</h4><ul><li>Home</li><li>About Us</li><li>Services &amp; Repairs</li><li>Contact</li></ul></div>
  <div class="fcol" style="left:662px"><h4>Sitemap</h4><ul><li>Online Store</li><li>Trips &amp; Charters</li><li>Events</li><li>Specials</li></ul></div>
  <div class="fcol hours" style="left:837px"><h4>Store Hours</h4><ul>
    <li><svg width="16" height="16" viewBox="0 0 16 16"><circle cx="8" cy="8" r="7" fill="none" stroke="#2a7bd0"/><path d="M8 4v4l3 2" stroke="#2a7bd0" fill="none"/></svg>Mon thru Sat - 10am to 6pm</li>
    <li><svg width="16" height="16" viewBox="0 0 16 16"><rect x="1" y="3" width="14" height="12" fill="none" stroke="#2a7bd0"/><path d="M1 7h14M5 1v4M11 1v4" stroke="#2a7bd0"/></svg>Closed on Sun</li>
    <li><svg width="16" height="16" viewBox="0 0 16 16"><path d="M8 15s5-5 5-9A5 5 0 0 0 3 6c0 4 5 9 5 9z" fill="none" stroke="#2a7bd0"/><circle cx="8" cy="6" r="2" fill="none" stroke="#2a7bd0"/></svg>14 Saltmere Plaza Saltmere, CT 06400</li>
  </ul></div>
</footer>
<div class="abs copyright">Copyright © 2021 Reefhollow - All Rights Reserved</div>

</body>
</html>
```